Wedding Invitation : Who helps to design a chic wedding card?

We need a chic invitation design for our wedding invitations.

FRONT

- Name logo : Mira & Joost
- Wedding date : zaterdag 9 juli 2022
- Quote : forever starts here

BACK

- Wij geven elkaar het ja-woord op zaterdag 9 juli 2022
Translation: We’ll say yes on Saturday 9th of July 2022 in the church of Ellebroek
- Timeline with icons:

o JAWOORD (Translation: We say yes)
o 15u00

o RECEPTIE (Translation: Reception)
o 18u30

o DINER (Translation: Dinner)
o 19u30
o Feestzaal Lorvendaal (Location)

o FEEST (Translation: Dinner)
o 21u30

- Locations:

o Icon of a church:
Ellebroek
o Icon of a location:
Feestzaal Lorvendaal
Burgemeester Tijskenslaan 47B
9870 Hoeveldorp

- RSVP Gelieve jouw aanwezigheid te bevestigen voor 29 mei 2022
(Translation: Please confirm before 29th of May 2022)

STYLE:

- Rosé gold relief press symbols
- Font style : handwritten or serif name (eg. playfair display)
- Font style: description in a more minimalistic font
- Cards will be in craft or ivory white, text will be in rosé gold relief press or black print

FORMAT
American format (229mm W x 114 mm H)

Target Market(s)

People 25-40 years old

Industry/Entity Type

Wedding / Event

Font styles to use
Serif
Sans Serif
Script

Colors

Designer to choose colors to be used in the design.

Requirements
Must have
• Name logo
Nice to have
• Minimalistic animation / icons
Should not have
• Jungle prints

```html
<!DOCTYPE html>
<html lang="nl">
<head>
<meta charset="utf-8">
<title>Huwelijksuitnodiging Mira &amp; Joost</title>
<link rel="stylesheet" href="https://fonts.googleapis.com/css2?family=Playfair+Display:ital,wght@0,400;0,700;1,700&family=Yellowtail&family=Sacramento&display=swap">
<style>
  :root {
    --backdrop: #f08a89;
    --paper: #fbfaf8;
    --rose-gold: #c9735a;
    --rose-gold-soft: #e39b83;
    --icon-tint: #f6ddd3;
  }
  * { box-sizing: border-box; margin: 0; padding: 0; }
  html, body { width: 1200px; height: 960px; overflow: hidden; }
  body { background: var(--backdrop); position: relative; font-family: "Playfair Display", Georgia, serif; }

  .card { position: absolute; top: 144px; width: 334px; height: 672px; background: var(--paper); }
  .card--front { left: 219px; }
  .card--back { left: 635px; }
  .abs { position: absolute; }

  /* Front */
  .name-mark {
    left: 0; width: 100%; top: 100px; text-align: center;
    font-family: "Playfair Display", Georgia, serif; font-weight: 400;
    font-size: 24px; color: var(--rose-gold); letter-spacing: .5px;
  }
  .couple-names { left: 0; width: 100%; top: 210px; text-align: center; color: var(--rose-gold); font-family: "Yellowtail", cursive; }
  .couple-names .first { display: block; font-size: 96px; line-height: 1; transform: translateX(22px); }
  .couple-names .and { display: block; font-family: "Sacramento", cursive; font-size: 30px; line-height: .6; }
  .couple-names .second { display: block; font-size: 96px; line-height: 1; transform: translateX(-6px); }
  .tagline { left: 0; width: 100%; top: 440px; text-align: center; font-family: "Sacramento", cursive; font-size: 28px; color: var(--rose-gold); }
  .weekday { left: 0; width: 100%; top: 510px; text-align: center; font-style: italic; font-weight: 700; font-size: 22px; color: var(--rose-gold); }
  .weekday-rule { top: 0; left: 0; }
  .date-row { top: 555px; left: 0; width: 100%; height: 62px; color: var(--rose-gold); font-size: 58px; line-height: 1; }
  .date-row span { position: absolute; top: 0; }
  .date-row .day { left: 50px; }
  .date-row .month { left: 135px; }
  .date-row .year { left: 240px; }
  .date-row .divider { position: absolute; top: -2px; width: 1px; height: 60px; background: var(--rose-gold); }

  /* Back */
  .intro { left: 0; width: 100%; top: 40px; text-align: center; color: var(--rose-gold-soft); font-size: 15.5px; line-height: 18px; }
  .timeline-art { left: 0; top: 0; }
  .step { color: var(--rose-gold-soft); }
  .step--left { text-align: right; right: 207px; }
  .step--right { left: 198px; }
  .step-label { font-style: italic; font-weight: 700; font-size: 13px; line-height: 14px; display: block; }
  .step-time { font-size: 20px; line-height: 20px; display: block; }
  .step-place { font-size: 8px; line-height: 12px; display: block; color: var(--rose-gold); }
  .venue-church { left: 20px; width: 96px; top: 510px; text-align: center; font-weight: 700; font-size: 12.5px; color: var(--rose-gold); }
  .venue-hall { left: 161px; top: 476px; color: var(--rose-gold); }
  .venue-hall .title { font-weight: 700; font-size: 13px; line-height: 15px; display: block; color: var(--rose-gold-soft); }
  .venue-hall .line { font-size: 9px; line-height: 12px; display: block; color: var(--rose-gold-soft); }
  .name-mark--back { top: 566px; font-size: 18px; }
  .rsvp { left: 0; width: 100%; top: 626px; text-align: center; font-size: 7.5px; color: var(--rose-gold); }
</style>
</head>
<body>

<section class="card card--front" aria-label="Voorzijde uitnodiging">
  <div class="abs name-mark">Mira &amp; Joost</div>

  <h1 class="abs couple-names">
    <span class="first">Mira</span>
    <span class="and">and</span>
    <span class="second">Joost</span>
  </h1>

  <p class="abs tagline">forever starts here...</p>

  <svg class="abs weekday-rule" width="334" height="672" aria-hidden="true">
    <line x1="90" y1="529" x2="116" y2="529" stroke="var(--rose-gold)" stroke-width="1"/>
    <circle cx="116" cy="529" r="1.6" fill="var(--rose-gold)"/>
    <line x1="224" y1="529" x2="250" y2="529" stroke="var(--rose-gold)" stroke-width="1"/>
    <circle cx="224" cy="529" r="1.6" fill="var(--rose-gold)"/>
  </svg>
  <p class="abs weekday">Zaterdag</p>

  <div class="abs date-row">
    <span class="day">09</span>
    <i class="divider" style="left:117px"></i>
    <span class="month">Juli</span>
    <i class="divider" style="left:224px"></i>
    <span class="year">22</span>
  </div>
</section>

<section class="card card--back" aria-label="Achterzijde uitnodiging">
  <p class="abs intro">Wij geven elkaar het ja-woord op<br>zaterdag 9 juli 2022</p>

  <svg class="abs timeline-art" width="334" height="672">
    <g stroke="var(--rose-gold-soft)" stroke-width="1" fill="none">
      <line x1="163" y1="166" x2="163" y2="196"/>
      <line x1="163" y1="261" x2="163" y2="291"/>
      <line x1="163" y1="356" x2="163" y2="386"/>
      <circle cx="163" cy="133" r="25"/>
      <circle cx="163" cy="228" r="25"/>
      <circle cx="163" cy="323" r="25"/>
      <circle cx="163" cy="418" r="25"/>
      <line x1="114" y1="465" x2="114" y2="523" stroke="var(--rose-gold)"/>
      <circle cx="140" cy="494" r="13"/>
    </g>
    <g fill="var(--icon-tint)">
      <circle cx="163" cy="133" r="16" role="img" aria-label="Icoon: bruidspaar"/>
      <circle cx="163" cy="228" r="16" role="img" aria-label="Icoon: bloemenboog"/>
      <circle cx="163" cy="323" r="16" role="img" aria-label="Icoon: bord met bestek"/>
      <circle cx="163" cy="418" r="16" role="img" aria-label="Icoon: klinkende glazen"/>
      <rect x="47" y="462" width="42" height="44" rx="3" role="img" aria-label="Icoon: kerkje"/>
    </g>
    <path d="M140 487a5 5 0 0 1 5 5c0 4-5 9-5 9s-5-5-5-9a5 5 0 0 1 5-5z" fill="none" stroke="var(--rose-gold)" stroke-width="1"/>
    <circle cx="140" cy="492" r="1.6" fill="var(--rose-gold)"/>
  </svg>

  <div class="abs step step--left" style="top:118px">
    <span class="step-label">Jawoord</span><span class="step-time">15:00</span>
  </div>
  <div class="abs step step--right" style="top:212px">
    <span class="step-label">Receptie</span><span class="step-time">18:30</span>
  </div>
  <div class="abs step step--left" style="top:307px">
    <span class="step-label">Diner</span><span class="step-time">19:30</span>
    <span class="step-place">Feestzaal Lorvendaal</span>
  </div>
  <div class="abs step step--right" style="top:402px">
    <span class="step-label">Feest</span><span class="step-time">21:30</span>
    <span class="step-place">Feestzaal Lorvendaal</span>
  </div>

  <div class="abs venue-church">Ellebroek</div>
  <address class="abs venue-hall" style="font-style:normal">
    <span class="title">Feestzaal Lorvendaal</span>
    <span class="line">Burgemeester Tijskenslaan 47B</span>
    <span class="line">9870 Hoeveldorp</span>
  </address>

  <div class="abs name-mark name-mark--back">Mira &amp; Joost</div>

  <p class="abs rsvp">- RSVP Gelieve jouw aanwezigheid te bevestigen voor 29 mei 2022</p>
  <svg class="abs" style="left:0;top:0" width="334" height="672" aria-hidden="true">
    <line x1="50" y1="640" x2="289" y2="640" stroke="var(--rose-gold-soft)" stroke-width=".6"/>
  </svg>
</section>

</body>
</html>
```